If everything digital fails, here's what to do

Hi, I would like a poster / infographic of a list of practical actions people could take in case the internet stops working. I've put together a list of 8 areas, with the situation for each, and the mitigation actions folks can take - I need it presented in a clear and aesthetically pleasing way. I will send you the file with the full text so you can include it all

Target Market(s)

General population, but likely people who are safety conscious and want to protect themselves and learn more about what to do to be tech literate and prepared

Industry/Entity Type

Tech / Cyber / Public safety / Civic tech

Font styles to use
Sans Serif

Requirements
Must have
• It's a lot of text, so I think the important thing is to have it all in one poster, or in a series of similar pages
Nice to have
• I would like it to be a bit brooding, but also elicit competence and that some experts have thought about this and it will all be okay
Should not have
• I don't want it to look cartoonish, or cheap - less is more is sort of what I'm looking for

```html
<!DOCTYPE html>
<html lang="en">
<head>
<meta charset="utf-8">
<title>If Everything Digital Fails, Here's What To Do</title>
<link href="https://fonts.googleapis.com/css2?family=Audiowide&family=Barlow+Condensed:wght@400;500;600;700&display=swap" rel="stylesheet">
<style>
  :root {
    --canvas: #ffffff;
    --navy: #1b2a7a;
    --deep-blue: #1d3f9e;
    --electric: #2d8fe0;
    --cyan: #5fd4ec;
    --violet: #8a45d6;
    --magenta: #b04fd8;
    --ink: #111a33;
    --label: #2b7fd4;
    --line: #3a8fdc;
    --white: #ffffff;
  }
  * { box-sizing: border-box; margin: 0; padding: 0; }
  html, body { width: 1200px; height: 1200px; overflow: hidden; background: var(--canvas); }
  body { position: relative; font-family: "Barlow Condensed", "Arial Narrow", sans-serif; color: var(--ink); }

  .poster {
    position: absolute; left: 52px; top: 216px; width: 1098px; height: 774px; overflow: hidden;
    background: linear-gradient(180deg, #1a2f8c 0%, #2456b8 30%, #3f5fc4 60%, #7b4ad0 85%, #a451d6 100%);
  }
  .backdrop-art {
    position: absolute; left: 230px; top: 0; width: 640px; height: 774px;
    background:
      radial-gradient(ellipse 55% 30% at 50% 38%, rgba(150,240,255,.95) 0%, rgba(60,170,240,.6) 45%, rgba(40,90,200,0) 100%),
      radial-gradient(ellipse 70% 45% at 50% 25%, rgba(70,190,250,.7) 0%, rgba(30,80,190,0) 100%);
  }

  .headline { position: absolute; left: 300px; top: 22px; width: 500px; text-align: center; font-family: "Audiowide", sans-serif; color: var(--white); }
  .headline .line-top { font-size: 31px; letter-spacing: 1px; text-shadow: 0 2px 6px rgba(10,20,80,.6); }
  .headline .line-fails {
    display: inline-block; margin: 4px 0 2px; padding: 0 26px; font-size: 52px; letter-spacing: 6px; line-height: 1.05;
    color: transparent; -webkit-text-stroke: 2px var(--white);
    background: linear-gradient(90deg, rgba(138,69,214,0) 0%, rgba(138,69,214,.95) 20%, rgba(176,79,216,.95) 80%, rgba(138,69,214,0) 100%);
  }
  .headline .line-bottom { font-size: 31px; letter-spacing: 1px; text-shadow: 0 2px 6px rgba(10,20,80,.6); }
  .headline .underline { border-bottom: 3px solid var(--violet); }

  .card { position: absolute; background: var(--white); padding: 7px 8px 8px; display: flex; flex-direction: column; }
  .card-head {
    display: flex; align-items: center; gap: 7px; height: 52px; padding: 0 7px; border-radius: 3px; flex: none;
    background: linear-gradient(90deg, #2a86d6 0%, #5cc6ec 100%); color: var(--white);
  }
  .card--light .card-head { background: linear-gradient(90deg, #4ec5ea 0%, #a5e8f2 100%); }
  .card-icon { width: 34px; height: 34px; flex: none; }
  .card-head-text { min-width: 0; }
  .card-title { font-family: "Audiowide", sans-serif; font-size: 13px; letter-spacing: .5px; line-height: 1; white-space: nowrap; }
  .card-title--two-line { white-space: normal; font-size: 12.5px; }
  .card-sub { font-size: 9.8px; font-weight: 500; color: var(--navy); line-height: 1.1; margin-top: 2px; }
  .label { text-align: center; font-size: 8.5px; font-weight: 700; letter-spacing: 1.3px; color: var(--label); margin: 5px 0 4px; flex: none; }
  .mitigations {
    flex: 1; border: 1.3px solid var(--line); border-radius: 9px; padding: 7px 8px;
    font-size: 9.2px; line-height: 1.16; font-weight: 500; overflow: hidden;
  }
  .mitigations strong { font-weight: 700; }
  .refresh { color: var(--label); font-weight: 700; text-decoration: underline; }
  .item { display: flex; gap: 6px; margin-bottom: 5px; }
  .item:last-child { margin-bottom: 0; }
  .item-num { font-family: "Audiowide", sans-serif; font-size: 18px; color: var(--deep-blue); line-height: 1; width: 13px; flex: none; }
  .mitigations p + p { margin-top: 5px; }

  .comms { left: 22px; top: 21px; width: 245px; height: 502px; }
  .tech-devices { left: 834px; top: 21px; width: 244px; height: 502px; }
  .banking-cash { left: 298px; top: 309px; width: 254px; height: 214px; }
  .info-passwords { left: 563px; top: 309px; width: 251px; height: 214px; }
  .transport { left: 22px; top: 534px; width: 245px; height: 226px; }
  .banking-records { left: 298px; top: 534px; width: 254px; height: 226px; }
  .info-cloud { left: 563px; top: 534px; width: 251px; height: 226px; }
  .tech-home { left: 834px; top: 534px; width: 244px; height: 226px; }
  .info-cloud .mitigations, .banking-records .mitigations { font-size: 8.8px; line-height: 1.14; }
</style>
</head>
<body>
<main class="poster">
  <div class="backdrop-art" role="img" aria-label="Broken steel chain links shattering apart over a glowing blue digital code background"></div>

  <header class="headline">
    <div class="line-top">IF EVERYTHING DIGITAL</div>
    <div class="line-fails">FAILS</div>
    <div class="line-bottom">HERE'S WHAT <span class="underline">TO</span> DO</div>
  </header>

  <section class="card comms">
    <div class="card-head">
      <svg class="card-icon" viewBox="0 0 40 40" fill="none" stroke="#fff" stroke-width="2"><rect x="17" y="4" width="14" height="24" rx="2"/><line x1="22" y1="24" x2="26" y2="24"/><path d="M5 30h20v6H5z"/><path d="M7 30c0-4 3-6 8-6s8 2 8 6"/></svg>
      <div class="card-head-text"><div class="card-title">COMMUNICATIONS</div><div class="card-sub">Cell phones / land-line phone services have stopped working</div></div>
    </div>
    <div class="label">POSSIBLE MITIGATIONS</div>
    <div class="mitigations">
      <div class="item"><span class="item-num">1</span><div><strong>Buy a two-way hand-held walkie talkie &amp; share the other with close friends.</strong><br><span class="refresh">Refresh when?</span> Check to ensure your walkie talkie has working batteries every 12 months (and that you know / remember how the walkie talkie itself works)</div></div>
      <div class="item"><span class="item-num">2</span><div><strong>Share a 'third space' safe spot with close contacts in town where you know you could meet in emergency situations if your home was not safe to remain in. Do the same with neighbours and folks who live in your neighbourhood - have a central gathering spot in your hood that you share with others so you can have a convening spot close by.</strong><br><span class="refresh">Refresh when?</span> Have a quick reminder conversation about this with your close contacts every 12 months to ensure everyone knows that's the plan</div></div>
      <div class="item"><span class="item-num">3</span><div><strong>Have a printed list of your close contacts' home addresses handy, if you don't know how to get to their places by heart.</strong><br><span class="refresh">Refresh when?</span> Print a new such document every 12 months to ensure it stays up to date</div></div>
      <div class="item"><span class="item-num">4</span><div><strong>Have a list of close contacts that might still have a working landline (ie. rotary, not voip-based), or who have a satellite phone</strong><br><span class="refresh">Refresh when?</span> Remind yourself of this list and refresh it every 12 months or so</div></div>
      <div class="item"><span class="item-num">5</span><div><strong>Make a list of the people in your life that you care about that may also be affected, and make sure you include individuals in your community that may be vulnerable in such a disruption (they may be older, may live alone, might need access to supply of medication).</strong><br><span class="refresh">Refresh when?</span> Remind yourself of this list and refresh it every 12 months or so</div></div>
    </div>
  </section>

  <section class="card tech-devices">
    <div class="card-head">
      <svg class="card-icon" viewBox="0 0 40 40" fill="none" stroke="#fff" stroke-width="2"><rect x="3" y="8" width="24" height="16" rx="1"/><line x1="10" y1="30" x2="20" y2="30"/><line x1="15" y1="24" x2="15" y2="30"/><rect x="29" y="14" width="9" height="16" rx="1.5"/></svg>
      <div class="card-head-text"><div class="card-title">TEHNOLOGY</div><div class="card-sub">Computers (laptops, tablets, smart phones) have stopped working</div></div>
    </div>
    <div class="label">POSSIBLE MITIGATIONS</div>
    <div class="mitigations">
      <div class="item"><span class="item-num">1</span><div><strong>Save all important digital materials (e.g. photos) that don't also exist on paper on a portable hard drive. Remember to do this for all digital materials that have been saved to your cloud that you might have forgotten about (archived, etc.).</strong><br><br><span class="refresh">Refresh when?</span> Do a backup and update every 6 months<br>Note: Since this is time-consuming, put a note in your calendar at the beginning of the year, choosing the time and date when you will do this (as noted in #5 above, you could do this in line with the solstice each year: June 20 and December 20)</div></div>
      <div class="item"><span class="item-num">2</span><div><strong>Get a hand cranked radio to ensure you have access to important news and information about what's happening in your community (locally, as well as nationally/internationally).</strong><br><span class="refresh">Refresh when?</span> Make sure the hand cranked radio has fresh batteries (change them every 12 months or so)</div></div>
      <div class="item"><span class="item-num">3</span><div><strong>Download a copy of your city's maps (e.g. Wayfind Maps) on your phone for local access, and make sure you have a physical map in case you need to get somewhere new in your city in a rush, and you don't know how to get there.</strong><br><span class="refresh">Refresh when?</span> N/A once done</div></div>
    </div>
  </section>

  <section class="card card--light banking-cash">
    <div class="card-head">
      <svg class="card-icon" viewBox="0 0 40 40" fill="none" stroke="#fff" stroke-width="2"><rect x="4" y="9" width="32" height="22" rx="2"/><line x1="4" y1="15" x2="36" y2="15"/><line x1="9" y1="24" x2="18" y2="24"/></svg>
      <div class="card-head-text"><div class="card-title">BANKING</div><div class="card-sub">Debit and credit cards have stopped working (in stores; ATMs)</div></div>
    </div>
    <div class="label">POSSIBLE MITIGATIONS</div>
    <div class="mitigations">
      <p><strong>Have $500 in cash available in $20 bills.</strong><br><span class="refresh">Refresh when?</span> N/A once done</p>
    </div>
  </section>

  <section class="card card--light info-passwords">
    <div class="card-head">
      <svg class="card-icon" viewBox="0 0 40 40" fill="none" stroke="#fff" stroke-width="2"><rect x="3" y="20" width="34" height="14" rx="2"/><path d="M14 20v-6a6 6 0 0 1 12 0v6"/><text x="20" y="31" font-size="9" fill="#fff" stroke="none" text-anchor="middle" font-family="sans-serif">***</text></svg>
      <div class="card-head-text"><div class="card-title card-title--two-line">INFORMATION MANAGEMENT</div><div class="card-sub">Password manager services (cloud) have stopped working</div></div>
    </div>
    <div class="label">POSSIBLE MITIGATIONS</div>
    <div class="mitigations">
      <p>Preamble: Many individuals don't remember their passwords anymore, having password managers generate complicated strings of characters as their passwords for their many digital accounts in their lives. <strong>Print a full list of your accounts and their passwords and keep that document safely in your living space.</strong><br><span class="refresh">Refresh when?</span> Print a new such document every 6 months to ensure the list remains up to date</p>
    </div>
  </section>

  <section class="card transport">
    <div class="card-head">
      <svg class="card-icon" viewBox="0 0 40 40" fill="none" stroke="#fff" stroke-width="2"><rect x="6" y="6" width="16" height="28" rx="1"/><rect x="9" y="10" width="10" height="7"/><path d="M22 14l6 4v12a2 2 0 0 0 4 0V16l-4-5"/></svg>
      <div class="card-head-text"><div class="card-title">TRANSPORTATIONS</div><div class="card-sub">Gas stations have stopped working</div></div>
    </div>
    <div class="label">POSSIBLE MITIGATIONS</div>
    <div class="mitigations">
      <p><strong>(If you own a car)<br>Have a standard 40L gas canister filled with gas and available close by in case needed.</strong></p>
      <p><span class="refresh">Refresh when?</span> Use up the gas within 4 months or so, and refill the canister then (i.e. 3 times a year) so that it remains usable</p>
      <p><span class="refresh">Safety note:</span> (If relevant) ensure the can is not in a place where kids can get to it, since it's not safe for kids to be around gas</p>
    </div>
  </section>

  <section class="card card--light banking-records">
    <div class="card-head">
      <svg class="card-icon" viewBox="0 0 40 40" fill="none" stroke="#fff" stroke-width="2"><path d="M4 14L20 5l16 9z"/><line x1="9" y1="17" x2="9" y2="29"/><line x1="16" y1="17" x2="16" y2="29"/><line x1="24" y1="17" x2="24" y2="29"/><line x1="31" y1="17" x2="31" y2="29"/><line x1="4" y1="33" x2="36" y2="33"/></svg>
      <div class="card-head-text"><div class="card-title">BANKING</div><div class="card-sub">Debit and credit cards have stopped working; your bank can't access its own information (online)</div></div>
    </div>
    <div class="label">POSSIBLE MITIGATIONS</div>
    <div class="mitigations">
      <p><strong>Print paper records of your banking statements that prove what you have in your bank accounts and store it in a safe place in your living space.</strong> Ensure it has dates showing and full amounts, as well as your identifiers (name and account numbers) as well as the institution itself (printed screenshots should work fine if your money is in a few accounts requiring many statements). Note the same goes for your liabilities (i.e. be able to prove how much you had left on your mortgage or other bigger loans, if you have such debt).<br><span class="refresh">Refresh when?</span> Update this document every 6-12 months</p>
    </div>
  </section>

  <section class="card card--light info-cloud">
    <div class="card-head">
      <svg class="card-icon" viewBox="0 0 40 40" fill="none" stroke="#fff" stroke-width="2"><path d="M11 18a7 7 0 0 1 13-4 6 6 0 0 1 7 6H9a4 4 0 0 1 2-2z"/><rect x="12" y="22" width="16" height="6" rx="1"/><rect x="12" y="29" width="16" height="6" rx="1"/></svg>
      <div class="card-head-text"><div class="card-title card-title--two-line">INFORMATION MANAGEMENT</div><div class="card-sub">Cloud storage services have stopped working</div></div>
    </div>
    <div class="label">POSSIBLE MITIGATIONS</div>
    <div class="mitigations">
      <p><strong>Do a backup of the important documents that are stored only in your cloud storage (e.g. that important email in your Postbox Mail; that tax document only issued digitally, etc.)</strong><br><span class="refresh">Refresh when?</span> Do a backup and update every 6 months<br>Note: Since this is a time-consuming exercise but not necessarily the same exercise as #7 below, you could alternate the months when you do one versus the other. For example, you could do this with annual equinoxes: March 21 and Sept 21 (pro tip: star email messages that are important as they arrive, so that you know what needs to be backed up every six months; that way, you don't have to go searching through your whole inbox)</p>
    </div>
  </section>

  <section class="card card--light tech-home">
    <div class="card-head">
      <svg class="card-icon" viewBox="0 0 40 40" fill="none" stroke="#fff" stroke-width="2"><path d="M5 19L20 7l15 12"/><path d="M9 16v17h22V16"/><path d="M15 25a7 7 0 0 1 10 0"/><path d="M17.5 28a3 3 0 0 1 5 0"/></svg>
      <div class="card-head-text"><div class="card-title">TEHNOLOGY</div><div class="card-sub">Smart home devices have stopped working</div></div>
    </div>
    <div class="label">POSSIBLE MITIGATIONS</div>
    <div class="mitigations">
      <p><strong>If you have a smart home device that needs to be connected to the internet to work and that doesn't have a manual override (e.g. a smart lock for your living space's main door, or for the garage) ensure you have a backup system in place that would not leave you stranded when the internet goes down.</strong><br><span class="refresh">Refresh when:</span> N/A once done</p>
    </div>
  </section>
</main>
</body>
</html>
```